Personal Training Studio Checkin App (or URL based)

I would like a simple web based app built for our  business. We have a training studio with a simple business model. All our clients buy sessions in packages either 4, 8, or 12 at a time. We want something that a trainer can pull up and Check in a client. This will record the date and time the client was checked in, by what trainer, and what type of session. This system will keep track of the following:
Whenever a Client Checks in so it will ‘tick off’ a session on their package (ie- they have gone from 11 sessions left to 10 sessions left)
Track what sessions a particular trainer does so we can pay them at the end of the week and look at who they trained, what type of session and how many
Look at client activity: Every time they check in, Recharge their package, any activity related to the client, even if it was admin – like deleting a session that was mistakenly recorded.
This will keep a database of clients added and all their activity
The pdf I have included lays out how I think it would work and the features I want
I would like this to run off an tablora that we have at our front check in counter. It can be an app or a URL that use.
***THIS PROJECT IS NOT SO MUCH ABOUT DESIGN BUT ABOUT FUNCTIONALITY OF THE APPLICATION. IT MUST HAVE THE FEATURES I HAVE ASKED FOR THAT WORK TOGETHER. I AM WILLING TO PAY A LITTLE MORE AS A BONUS IF YOU CAN ACCOMPLISH THIS. ALSO IF I FIN THE RIGHT PERSON THAT CAN DO THIS I WILL MAKE IT A GUARNTEED PROJECT.

- Functionality and Track and record all the info we need

```html
<!DOCTYPE html>
<html lang="en">
<head>
<meta charset="utf-8">
<title>Ironline Personal Training Studio – Choose an option</title>
<link href="https://fonts.googleapis.com/css2?family=Lato:wght@400;700&family=Roboto:wght@400;500;700&display=swap" rel="stylesheet">
<style>
  :root {
    --ink: #111827;
    --text: #374151;
    --muted: #e5e7eb;
    --card-bg: #f7f7f7;
    --card-border: #ececec;
    --brand: #ff6a2b;
    --brand-grey: #5f5f5f;
    --accent-top: #ff8552;
    --accent-bottom: #ff4400;
    --white: #ffffff;
  }
  * { box-sizing: border-box; margin: 0; padding: 0; }
  html, body { width: 1200px; height: 1110px; overflow: hidden; background: var(--white); }
  body { position: relative; font-family: "Roboto", Arial, sans-serif; color: var(--text); }

  .site-header {
    position: absolute; left: 0; top: 0; width: 1200px; height: 91px;
    border-bottom: 1px solid #efefef;
  }
  .brand-name {
    position: absolute; left: 33px; top: 14px;
    display: flex; align-items: center; gap: 10px;
    font-family: "Roboto", Arial, sans-serif; font-weight: 700;
    font-size: 30px; color: var(--brand-grey); letter-spacing: 0.5px;
  }
  .brand-name .brand-square {
    width: 22px; height: 22px; background: var(--brand); border-radius: 3px;
  }
  .brand-name .brand-sub { display: none; }
  .brand-tag {
    position: absolute; left: 35px; top: 56px;
    font-size: 8.5px; font-weight: 700; letter-spacing: 3px; color: var(--brand-grey);
  }

  .intro { position: absolute; left: 0; top: 192px; width: 1200px; text-align: center; }
  .intro h1 {
    font-family: "Lato", Arial, sans-serif; font-weight: 700;
    font-size: 31px; color: var(--ink); line-height: 44px;
  }
  .intro p { margin-top: 14px; font-size: 16.5px; line-height: 24px; color: var(--text); }

  .option {
    position: absolute; top: 355px; width: 276px; height: 237px;
    border-radius: 33px; background: var(--card-bg);
    border: 1px solid var(--card-border);
    box-shadow: 0 6px 16px rgba(0,0,0,0.05);
    text-decoration: none;
  }
  .option-checkin { left: 145px; }
  .option-new { left: 463px; }
  .option-admin {
    left: 781px; border: none;
    background: linear-gradient(180deg, var(--accent-top), var(--accent-bottom));
    box-shadow: none;
  }
  .option-icon {
    position: absolute; left: 79px; top: 41px; width: 118px; height: 118px;
    border-radius: 50%; border: 1.5px solid #e3e3e3;
    display: flex; align-items: center; justify-content: center;
  }
  .option-admin .option-icon { border: none; }
  .option-label {
    position: absolute; left: 0; width: 100%; top: 180px; text-align: center;
    font-family: "Lato", Arial, sans-serif; font-size: 19.5px; font-weight: 400; color: var(--ink);
  }
  .option-admin .option-label { color: var(--white); font-weight: 700; }
  .option-bar {
    position: absolute; top: 612px; width: 85px; height: 3px; border-radius: 2px; background: var(--muted);
  }

  .site-footer { position: absolute; left: 0; top: 786px; width: 1200px; text-align: center; }
  .footer-brand {
    display: inline-flex; align-items: center; gap: 9px;
    font-weight: 700; font-size: 28px; color: var(--brand-grey);
  }
  .footer-brand .brand-square { width: 20px; height: 20px; background: var(--brand); border-radius: 3px; }
  .footer-tag { margin-top: 4px; font-size: 8px; font-weight: 700; letter-spacing: 3px; color: var(--brand-grey); }
  .copyright { margin-top: 20px; font-size: 16px; color: var(--text); }
  .legal { position: absolute; left: 0; top: 986px; width: 1200px; text-align: center; font-size: 13px; color: var(--text); }
</style>
</head>
<body>
  <header class="site-header">
    <div class="brand-name"><span class="brand-square"></span>IRONLINE</div>
    <div class="brand-tag">PERSONAL TRAINING STUDIO</div>
  </header>

  <section class="intro">
    <h1>Choose an option:</h1>
    <p>Please choose one of the options below to get started. Your selection will help us guide you through the next steps.</p>
  </section>

  <a class="option option-checkin" href="#checkin">
    <span class="option-icon">
      <svg width="76" height="76" viewBox="0 0 76 76" fill="none" stroke="#ff6a2b" stroke-width="3.5" stroke-linecap="round" stroke-linejoin="round">
        <circle cx="19" cy="12" r="6"/>
        <circle cx="57" cy="12" r="6"/>
        <path d="M6 70V50c0-8 6-14 14-14h4c6 0 10 3 12 8"/>
        <path d="M24 50h10"/>
        <path d="M24 50v20"/>
        <path d="M57 26c-8 0-13 7-13 15 0 6 4 10 6 14l2 14h10l2-14c2-4 6-8 6-14 0-8-5-15-13-15z"/>
      </svg>
    </span>
    <span class="option-label">Client Check In</span>
  </a>
  <div class="option-bar" style="left:241px"></div>

  <a class="option option-new" href="#new-client">
    <span class="option-icon">
      <svg width="76" height="76" viewBox="0 0 76 76" fill="none" stroke="#ff6a2b" stroke-width="3.5" stroke-linecap="round" stroke-linejoin="round">
        <circle cx="32" cy="20" r="14"/>
        <path d="M8 68c0-14 10-24 24-24 6 0 11 2 15 5"/>
        <path d="M58 48v22M47 59h22"/>
      </svg>
    </span>
    <span class="option-label">Add New Client</span>
  </a>
  <div class="option-bar" style="left:559px"></div>

  <a class="option option-admin" href="#admin">
    <span class="option-icon">
      <svg width="76" height="76" viewBox="0 0 76 76" fill="none" stroke="#ffffff" stroke-width="4" stroke-linecap="round">
        <path d="M2 16h15M33 16h39"/><rect x="17" y="10" width="16" height="12" rx="6"/>
        <path d="M2 38h41M59 38h13"/><rect x="43" y="32" width="16" height="12" rx="6"/>
        <path d="M2 60h15M33 60h39"/><rect x="17" y="54" width="16" height="12" rx="6"/>
      </svg>
    </span>
    <span class="option-label">Admin Panel</span>
  </a>

  <footer class="site-footer">
    <div class="footer-brand"><span class="brand-square"></span>IRONLINE</div>
    <div class="footer-tag">PERSONAL TRAINING STUDIO</div>
    <p class="copyright">© 2025 All rights reserved.</p>
  </footer>
  <p class="legal">Use of this website constitutes acceptance of our User Agreement and Privacy Policy.</p>
</body>
</html>
```